Création d'un modèle de compte-rendus
Besoins
Cabinet de recrutement et de conseil en Ressources Humaines, nous intervenons depuis plus de 60 ans auprès d’entreprises afin de pourvoir leurs besoins en recrutement.
Nous intervenons sur tout type de postes, du cadre dirigeant à l’ouvrier, avec une majorité de postes à responsabilités.
Dans le cadre de nos recrutements, nous envoyons à l’entreprise cliente un document de synthèse des candidats intéressants que nous rencontrons. Dans ce document, nous présentons son parcours professionnel, ses informations générales (mobilité, préavis, rémunération…), ses principaux traits de personnalité, son potentiel intellectuel ainsi qu’une conclusion présentant les points forts, les axes de progrès et notre avis sur ce candidat.
Nos synthèses actuelles sont sous la forme d’un document WORD de 4 à 6 pages assez classique et nous souhaiterions avoir un document plus dynamique, tout en restant sobre. Les informations clés doivent être rapides à identifier et accessibles à l’œil facilement.
La cible :
Directeurs Généraux, Directeurs des Ressources Humaines, Responsable Recrutement
Tous secteurs d’activité
Groupes internationaux, Entreprises/Industries nationales ou locales, PME/PMI
Couleurs, favoris et autres exigences :
Cf notre logo et site internet : www.vornat-exemple.fr, tons bleus et blancs principalement
Sobriété, Simplicité
Nous sommes ouverts à toute proposition créative de votre part.

```html
<!DOCTYPE html>
<html lang="fr">
<head>
<meta charset="utf-8">
<title>Fiche candidat – Vornat Conseil</title>
<link rel="stylesheet" href="https://fonts.googleapis.com/css2?family=Raleway:wght@300;400&display=swap">
<style>
  :root {
    --brand-blue: #1a64a1;
    --soft-blue: #8296c6;
    --photo-dark: #1b1f24;
    --photo-mid: #3a4a55;
    --photo-teal: #6f94a3;
    --paper: #ffffff;
    --logo-blue: #2b78b4;
    --tagline-grey: #8a9aa8;
  }
  * { margin: 0; padding: 0; box-sizing: border-box; }
  html, body { width: 848px; height: 1200px; overflow: hidden; background: var(--paper); }
  .cover {
    position: relative;
    width: 848px;
    height: 1200px;
    background: var(--paper);
    font-family: "Raleway", sans-serif;
  }
  .cover-graphics { position: absolute; inset: 0; }
  .doc-title {
    position: absolute;
    left: 297px;
    top: 64px;
    width: 254px;
    height: 73px;
    display: flex;
    align-items: center;
    justify-content: center;
    color: var(--paper);
    font-weight: 300;
    font-size: 20px;
    letter-spacing: 0.5px;
  }
  .doc-title-frame { position: absolute; inset: 0; overflow: visible; }
  .brand {
    position: absolute;
    left: 0;
    top: 940px;
    width: 848px;
    text-align: center;
  }
  .brand-name {
    display: inline-flex;
    align-items: center;
    gap: 12px;
    color: var(--logo-blue);
    font-weight: 400;
    font-size: 46px;
    line-height: 1;
  }
  .brand-dot {
    width: 14px;
    height: 14px;
    border-radius: 50%;
    background: var(--logo-blue);
  }
  .brand-tagline {
    margin-top: 10px;
    color: var(--tagline-grey);
    font-weight: 400;
    font-size: 14px;
    letter-spacing: 1.4px;
  }
</style>
</head>
<body>
<main class="cover">
  <svg class="cover-graphics" width="848" height="1200" viewBox="0 0 848 1200" aria-hidden="false">
    <defs>
      <linearGradient id="photo-tones" x1="0" y1="1" x2="1" y2="0">
        <stop offset="0" stop-color="var(--photo-dark)"/>
        <stop offset="0.45" stop-color="var(--photo-mid)"/>
        <stop offset="1" stop-color="var(--photo-teal)"/>
      </linearGradient>
    </defs>
    <polygon class="header-band" points="0,0 848,0 848,148 0,495" fill="var(--brand-blue)"/>
    <polygon class="header-accent" points="0,163 537,268 0,482" fill="var(--soft-blue)"/>
    <polygon class="photo-band" role="img"
      aria-label="Photo : homme en costume tenant dans sa main un globe terrestre relié par un réseau de connexions"
      points="0,508 848,161 848,580 0,912" fill="url(#photo-tones)"/>
    <polygon class="corner-accent" points="537,721 848,594 848,834" fill="var(--brand-blue)"/>
  </svg>

  <div class="doc-title">
    <svg class="doc-title-frame" width="254" height="73" viewBox="0 0 254 73" aria-hidden="true">
      <polyline points="80,72 0,72 0,0 254,0 254,72 174,72"
        fill="none" stroke="#ffffff" stroke-opacity="0.7" stroke-width="1.2" stroke-dasharray="2 2"/>
    </svg>
    FICHE CANDIDAT
  </div>

  <div class="brand">
    <div class="brand-name"><span class="brand-dot"></span>Vornat Conseil</div>
    <div class="brand-tagline">Recrutement &amp; Ressources Humaines</div>
  </div>
</main>
</body>
</html>
```